Velmont Advisory e-Flyer Design

Need 6 or so one pagers done. To be used to email to clients. Each to look similar with slight variations. Attached is an example done for a completely different organization, but it has the style we are looking for, and it is energetic and corporate.

```html
<!DOCTYPE html>
<html lang="en">
<head>
<meta charset="utf-8">
<title>Velmont Advisory – e-Flyer</title>
<link href="https://fonts.googleapis.com/css2?family=Archivo+Black&family=Arimo:wght@400;700&display=swap" rel="stylesheet">
<style>
  :root {
    --brand-red: #d21f26;
    --white: #ffffff;
    --photo-light: #f4f5f7;
    --photo-mid: #d9dde3;
    --photo-blue: #a9c2de;
    --photo-grey: #8d9096;
  }
  * { box-sizing: border-box; margin: 0; padding: 0; }
  html, body { width: 1120px; height: 1200px; overflow: hidden; background: var(--white); }
  .flyer {
    position: relative;
    width: 1120px;
    height: 1200px;
    overflow: hidden;
    font-family: "Arimo", Arial, sans-serif;
    color: var(--white);
    background: var(--brand-red);
  }
  .hero-photo {
    position: absolute;
    left: 0; top: 0;
    width: 1120px; height: 700px;
    background:
      radial-gradient(ellipse at 18% 35%, var(--photo-blue) 0%, rgba(169,194,222,0) 45%),
      radial-gradient(ellipse at 45% 88%, var(--photo-grey) 0%, rgba(141,144,150,0) 38%),
      linear-gradient(160deg, var(--photo-light) 0%, var(--white) 45%, var(--photo-mid) 100%);
  }
  .tagline-ribbon {
    position: absolute;
    left: 229px; top: 637px;
    width: 626px; height: 63px;
  }
  .tagline {
    position: absolute;
    left: 265px; top: 653px;
    font-size: 20px;
    letter-spacing: 2.6px;
    white-space: nowrap;
  }
  .tagline .sep { margin: 0 14px; }
  .brand-tile {
    position: absolute;
    left: 54px; top: 559px;
    width: 175px; height: 215px;
    background: var(--white);
    display: flex;
    flex-direction: column;
    justify-content: center;
    align-items: center;
    color: var(--brand-red);
    font-weight: 700;
    font-size: 27px;
    line-height: 1.15;
    text-align: center;
  }
  .column {
    position: absolute;
    top: 823px;
  }
  .column h2 {
    font-family: "Archivo Black", "Arial Black", sans-serif;
    font-weight: 400;
    font-size: 20px;
    margin-bottom: 26px;
  }
  .column p {
    font-size: 19.2px;
    line-height: 25.6px;
  }
  .about { left: 59px; width: 280px; }
  .why { left: 401px; width: 372px; }
  .divider {
    position: absolute;
    top: 838px;
    width: 1px; height: 333px;
    background: var(--white);
  }
  .divider.first { left: 364px; }
  .divider.second { left: 798px; }
  .contact {
    position: absolute;
    left: 799px; top: 828px;
    width: 321px;
    list-style: none;
    text-align: center;
    font-size: 20.5px;
    line-height: 24px;
  }
  .contact li { display: flex; flex-direction: column; align-items: center; }
  .contact svg { display: block; margin-bottom: 6px; }
  .contact .phone { margin-bottom: 36px; }
  .contact .email { margin-bottom: 30px; }
</style>
</head>
<body>
<main class="flyer">
  <div class="hero-photo" role="img" aria-label="Bright office desk scene: a person in a light blue shirt writing in a notebook beside an open laptop, a phone and a potted plant"></div>

  <svg class="tagline-ribbon" viewBox="0 0 626 63" aria-hidden="true">
    <polygon points="0,0 585,0 626,63 0,63" fill="var(--brand-red)"/>
  </svg>
  <div class="tagline">STRATEGY<span class="sep">.</span>EXECUTION<span class="sep">.</span>PERFORMANCE</div>

  <div class="brand-tile"><span>Velmont</span><span>Advisory</span></div>

  <section class="column about">
    <h2>Who We Are</h2>
    <p>At Velmont Advisory, we specialize in strategy clarification and aligned execution. We are executives with global operations and front-line experience who help drive your business performance. Our proven Catalyst method works across industries, geographies, as well as organization types and sizes.</p>
  </section>

  <div class="divider first"></div>

  <section class="column why">
    <h2>Why Choose Velmont</h2>
    <p>Velmont brings you and each member of your team a framework of strategy clarification and aligned execution - the only true competitive differentiator for organizations today. Without that framework on matters big and small, organizations, at best, misuse time and resources and don't maximize performance potential, or, at worst case, lose market share or more. Nothing is left to chance with Velmont.</p>
  </section>

  <div class="divider second"></div>

  <ul class="contact">
    <li class="phone">
      <svg width="22" height="32" viewBox="0 0 22 32" aria-hidden="true">
        <path d="M6 2 L9 9 L6.5 11 C7.5 16 10 21 14 25 L16.5 23 L21 28 L17 31 C9 28 2 17 2 6 Z" fill="none" stroke="var(--white)" stroke-width="2.2" stroke-linejoin="round"/>
      </svg>
      <span>+1 555 014 2290</span>
    </li>
    <li class="email">
      <svg width="34" height="22" viewBox="0 0 34 22" aria-hidden="true">
        <rect x="1.5" y="1.5" width="31" height="19" fill="none" stroke="var(--white)" stroke-width="2.5"/>
        <path d="M1.5 1.5 L17 13 L32.5 1.5 M1.5 20.5 L13 10 M32.5 20.5 L21 10" fill="none" stroke="var(--white)" stroke-width="2.5"/>
      </svg>
      <span>hello@velmontadvisory.com</span>
    </li>
    <li class="address">
      <svg width="24" height="34" viewBox="0 0 24 34" aria-hidden="true">
        <path d="M12 0 C5.4 0 0 5.2 0 11.8 C0 20 12 34 12 34 C12 34 24 20 24 11.8 C24 5.2 18.6 0 12 0 Z M12 16.5 A4.8 4.8 0 1 1 12 6.9 A4.8 4.8 0 1 1 12 16.5 Z" fill="var(--white)" fill-rule="evenodd"/>
      </svg>
      <span>140 Harbor Lane #2,<br>Fairview, NY 10099</span>
    </li>
  </ul>
</main>
</body>
</html>
```